Web Design Project - veltrimo

I'm building an agency for marketing solutions but also medical education and patients education for pharmaceutical companies, medical societies and patient advocacy groups. We want to be perceived as the most innovative in the market. We work through design thinking solutions for campaigns and services.
I love some websites based on Swiss style design like www.plorvex.net
We are a small group of designers, physicians and creatives working together to deliver the best experiences in our market.
We decided to also use design crowd expecting that we maybe found a great idea we didn't thought about yet.
Updates

I'm extending it for more 2 weeks

Reason: I need the best design you can. Only PSD. No code needed. Love Swiss style, like qualdor 5 and plorvex.net I'm extending the deadline until get something great. Willing to extend as much as needed.

Target Market(s)

Pharmaceutical companies, physicians, medical societies, patients advocacy groups

Industry/Entity Type

Pharmaceutical

Font styles to use
Other font styles liked:
• Helvetia family

Colors

Designer to choose colors to be used in the design.

Requirements
Must have
• Must be innovative like www.plorvex.net
Nice to have
• Cool menus
Should not have
• Not to appear too much Comercial. We like to be a boutique in this market. Craftsmen working with less clients at time but delivering precious stones.

```html
<!DOCTYPE html>
<html lang="en">
<head>
<meta charset="utf-8">
<title>veltrimo</title>
<link rel="stylesheet" href="https://fonts.googleapis.com/css2?family=Arimo:wght@400;700&family=Open+Sans:wght@300;400;600&display=swap">
<style>
  :root {
    --teal: #00c4c6;
    --ink: #222;
    --body: #444;
    --grey: #b3b3b3;
    --bar: #454545;
    --white: #fff;
  }
  * { margin: 0; padding: 0; box-sizing: border-box; }
  html, body { width: 960px; height: 1200px; overflow: hidden; background: var(--white); }
  .page { position: relative; width: 960px; height: 1200px; font-family: "Open Sans", sans-serif; color: var(--body); }
  .abs { position: absolute; }

  /* header */
  .brand { left: 78px; top: 28px; font-family: "Arimo", sans-serif; font-size: 32px; color: var(--teal); letter-spacing: 0.5px; }
  .nav-icon { top: 34px; width: 30px; height: 30px; }
  .nav-divider { top: 29px; width: 1px; height: 39px; background: #ccc; }
  .nav-active { left: 481px; top: 71px; width: 50px; height: 2px; background: var(--ink); }

  /* hero */
  .hero { left: 0; top: 85px; width: 960px; height: 367px; background: var(--teal); }
  .photo { position: absolute; }
  .tile-pills { left: 81px; top: 106px; width: 196px; height: 158px; background: linear-gradient(135deg, #3e4a4a, #25302f); }
  .tile-laptop { left: 81px; top: 268px; width: 196px; height: 158px; background: linear-gradient(135deg, #cfd6e0, #8694ad 60%, #3b4660); }
  .tile-sketch { left: 282px; top: 106px; width: 196px; height: 318px; background: linear-gradient(180deg, #e6e6e6, #cfcfcf 60%, #5a5a5a); }
  .tile-lab { left: 482px; top: 106px; width: 396px; height: 156px; background: linear-gradient(90deg, #e4e8ec, #9aa4ae 50%, #b38c72); }
  .plus-box { left: 163px; top: 167px; width: 34px; height: 31px; background: var(--white); border-radius: 2px; }
  .welcome-title { left: 506px; top: 266px; font-family: "Arimo", sans-serif; font-size: 26px; color: var(--white); white-space: nowrap; }
  .welcome-title .name { font-size: 35px; color: var(--ink); margin-left: 8px; }
  .welcome-text { left: 506px; top: 310px; width: 380px; font-size: 18px; font-weight: 300; line-height: 29px; color: var(--white); letter-spacing: 0.6px; }
  .welcome-text strong { font-weight: 600; }

  /* societies */
  .tile-doctors { left: 78px; top: 480px; width: 253px; height: 170px; background: linear-gradient(135deg, #e3ddd6, #c9c3bd 50%, #f2f2f2); }
  .section-title { left: 372px; top: 470px; font-size: 42px; font-weight: 300; color: var(--teal); letter-spacing: 1.5px; white-space: nowrap; }
  .section-text { left: 373px; top: 527px; width: 520px; font-size: 22px; font-weight: 300; line-height: 30.5px; color: var(--body); letter-spacing: 1.2px; }

  /* service cards */
  .card { position: absolute; top: 716px; width: 242px; height: 182px; overflow: hidden; }
  .card-pharma { left: 80px; background: linear-gradient(135deg, #f4f0ee, #d9cfc9 50%, #b8b0ad); }
  .card-marketing { left: 360px; background: linear-gradient(135deg, #eeeeee, #cfd1d4 50%, #9a9a9a); }
  .card-education { left: 638px; background: linear-gradient(135deg, #d6dbe3, #8a97ae 55%, #394460); }
  .card-label { position: absolute; left: 0; bottom: 0; width: 100%; height: 36px; background: rgba(255,255,255,0.85); font-family: "Arimo", sans-serif; font-weight: 700; font-size: 19px; color: var(--ink); letter-spacing: 1px; text-align: center; line-height: 36px; }

  /* footer */
  .contact-box { left: 80px; top: 936px; width: 516px; height: 204px; background: var(--grey); color: var(--white); font-family: "Arimo", sans-serif; }
  .contact-name { position: absolute; left: 14px; top: 10px; font-size: 42px; letter-spacing: 1px; }
  .contact-row { position: absolute; left: 16px; display: flex; align-items: center; gap: 12px; font-size: 18px; letter-spacing: 0.4px; white-space: nowrap; }
  .contact-row svg { width: 12px; height: 12px; flex: none; }
  .contact-row.small { font-size: 14px; }
  .promo-box { left: 636px; top: 936px; width: 242px; height: 203px; background: var(--teal); }
  .promo-title { position: absolute; left: 12px; top: 22px; font-family: "Arimo", sans-serif; font-size: 23px; color: var(--white); white-space: nowrap; }
  .promo-title span { font-size: 29px; color: var(--ink); }
  .promo-text { position: absolute; left: 14px; top: 60px; width: 220px; font-size: 16px; font-weight: 300; line-height: 23px; color: var(--white); letter-spacing: 1px; }
  .bottom-bar { left: 0; top: 1170px; width: 960px; height: 30px; background: var(--bar); color: var(--white); font-family: "Arimo", sans-serif; font-size: 13px; text-align: center; line-height: 30px; }
</style>
</head>
<body>
<div class="page">

  <header>
    <div class="abs brand">veltrimo</div>
    <nav>
      <svg class="abs nav-icon" style="left:491px" viewBox="0 0 30 30" fill="none" stroke="#222" stroke-width="2"><path d="M3 15 L15 4 L27 15"/><path d="M7 12 V27 H13 V19 H17 V27 H23 V12"/><path d="M21 8 V4 H24 V11"/></svg>
      <div class="nav-active abs"></div>
      <div class="abs nav-divider" style="left:552px"></div>
      <svg class="abs nav-icon" style="left:582px" viewBox="0 0 30 30" fill="none" stroke="#222" stroke-width="2"><rect x="2" y="8" width="26" height="19" rx="2"/><path d="M11 8 V4 H19 V8"/><path d="M15 12 V23 M9.5 17.5 H20.5" stroke-width="2.5"/></svg>
      <div class="abs nav-divider" style="left:640px"></div>
      <svg class="abs nav-icon" style="left:670px" viewBox="0 0 30 30" fill="none" stroke="#222" stroke-width="2"><path d="M10 20 C5 16 6 7 15 7 C24 7 25 16 20 20 V23 H10 Z"/><path d="M11 26 H19"/><path d="M15 1 V4 M4 6 L6 8 M26 6 L24 8 M1 15 H3 M27 15 H29"/></svg>
      <div class="abs nav-divider" style="left:728px"></div>
      <svg class="abs nav-icon" style="left:748px" viewBox="0 0 30 30" fill="none" stroke="#222" stroke-width="2"><rect x="9" y="1" width="12" height="4"/><path d="M10 5 V8 L7 11 V28 H23 V11 L20 8 V5"/><path d="M15 14 V24 M10 19 H20"/></svg>
      <svg class="abs nav-icon" style="left:841px" viewBox="0 0 30 30" fill="none" stroke="#222" stroke-width="2"><rect x="2" y="5" width="26" height="19" rx="3"/><circle cx="10" cy="12" r="3"/><path d="M5 20 C6 16 14 16 15 20"/><path d="M18 11 H25 M18 15 H25"/><path d="M8 24 V27 M22 24 V27"/></svg>
    </nav>
  </header>

  <section class="abs hero" aria-label="Welcome"></section>
  <div class="photo tile-pills" role="img" aria-label="Close-up of assorted capsules and tablets in dark tones"></div>
  <div class="abs plus-box"><svg viewBox="0 0 34 31" width="34" height="31"><path d="M17 8 V23 M9.5 15.5 H24.5" stroke="#222" stroke-width="3"/></svg></div>
  <div class="photo tile-laptop" role="img" aria-label="Woman typing on a laptop"></div>
  <div class="photo tile-sketch" role="img" aria-label="Businessman drawing business sketches on a wall"></div>
  <div class="photo tile-lab" role="img" aria-label="Smiling scientist working at a microscope"></div>
  <h1 class="abs welcome-title">welcome to<span class="name">veltrimo</span></h1>
  <p class="abs welcome-text">simply dummy text of the printing and typesetting industry. Excepteur sint occaecat cupidatat <strong>Lorem Ipsum</strong> has been the industry's the took a galley.</p>

  <div class="photo tile-doctors" role="img" aria-label="Smiling team of doctors and nurses"></div>
  <h2 class="abs section-title">Medical societies</h2>
  <p class="abs section-text">simply dummy text of the printing and typesetting industry. Lorem Ipsum has been the industry's standard dummy text ever since the 1500s, when an unknown a galley.</p>

  <div class="card card-pharma" role="img" aria-label="Capsules and tablets on a white surface"><div class="card-label">Pharmaceutical</div></div>
  <div class="card card-marketing" role="img" aria-label="Team reviewing charts around a table"><div class="card-label">Marketing Solutions</div></div>
  <div class="card card-education" role="img" aria-label="Woman typing on a laptop"><div class="card-label">Patients Education</div></div>

  <footer>
    <div class="abs contact-box">
      <div class="contact-name">veltrimo</div>
      <div class="contact-row" style="top:76px"><svg viewBox="0 0 12 12"><path d="M2 1 L4.5 1 L5.5 3.5 L4 4.5 C4.8 6.3 5.7 7.2 7.5 8 L8.5 6.5 L11 7.5 V10 C6 11 1 6 2 1 Z" fill="#333"/></svg>+44 1632 960418</div>
      <div class="contact-row" style="top:108px"><svg viewBox="0 0 12 12"><rect x="1" y="3" width="10" height="7" fill="#333"/><path d="M1 3 L6 7 L11 3" stroke="#b3b3b3" fill="none"/></svg>info@veltrimo.com</div>
      <div class="contact-row" style="top:143px"><svg viewBox="0 0 12 12"><path d="M6 11 C2 6 2 5 2 4.5 A4 4 0 0 1 10 4.5 C10 5 10 6 6 11 Z" fill="#333"/><circle cx="6" cy="4.5" r="1.5" fill="#b3b3b3"/></svg>27 Harlow Lane, Brenford, BN4 2TX, UK</div>
      <div class="contact-row small" style="top:176px"><svg viewBox="0 0 12 12"><circle cx="6" cy="6" r="5" fill="none" stroke="#333" stroke-width="1.2"/><path d="M7.8 4.5 A2.2 2.2 0 1 0 7.8 7.5" fill="none" stroke="#333" stroke-width="1.2"/></svg>2014 veltrimo. All Rights Reserved I Privacy Policy</div>
    </div>
    <div class="abs promo-box">
      <div class="promo-title">medical <span>societies</span></div>
      <p class="promo-text">Lorem Ipsum has been the industry's standard dummy text ever since the 1500s, when an unknown printer</p>
    </div>
    <div class="abs bottom-bar">© &nbsp;2014 veltrimo. All Rights Reserved I Privacy Policy</div>
  </footer>

</div>
</body>
</html>
```